Exciting opportunity to design soap packaging for niche market with huge potential!

We need a packaging design for a new business and product hitting the martial arts industry soon.

Product:
Soap that aids with muscle recovery and reduces risk of infections.

Product Colour:
Black

Brand slogan:
RIVET STAPLES
(This is a registered trademark)

Brand font:
I'm thinking Proxima Nova but open to suggestions.

Brand Inspiration:
I really like Tallwind Apparel, Korvell Matgear, Brisko UTL branding.
Target Market: Combat athletes ie. MMA Fighters, Jiu Jitsu athletes, Wrestlers.

Brands Mission:
We aim to educate our market and bring gym hygiene to the forefront of combat athletes minds. We also aim to help our athletes recover easier and train longer by adding in Magnesium and soothing oils to the product.

How we aim to be perceived:
Modern, contemporary, minimalist, premium but affordable, sleek and stylish, reliable and organic.

The packaging color can be altered, but we intend to manufacture on a sleeve style box, see attached images.

Preferred color palette is monochromatic but please take a creative lead.

If possible please provide mock ups and on die lines, provide correct file types that should allow to be sized on to any die lines.

*NOTE*
In MMA, BJJ, and wrestling, due to the nature of the skin on skin sweating skin infections like staph and ringworm are very prominent, this soap is aimed to reduce infection in schools by using natures oils to kill the bacteria.
Featured ingredients are Magnesium, Eucalyptus & Tea Tree Oil, and Activated Charcoal.
Activated charcoal facilitates a deep clean.
Eucalyptus and teatree for their antibacterial properties.
Peppermint and magnesium to soothe sore muscles.
The Soap is VERY moisturising with a base comprised of Olive Oil, Coconut Oil and Shea Butter.

Target Market(s)

Combat Athletes ie. MMA Fighters, BJJ Athletes, Wrestlers

Industry/Entity Type

Combat industry, Mixed Martial Arts, Brazilian Jiu Jitsu, Wrestling

Font styles to use
Sans Serif
Other font styles liked:
• Proxima Nova

Requirements
Must have
• Space for Product Description, Ingredients List, Caution, Directions for use, website url, business address, made in australia, product weight front and back. Design all 6 sides of box not just front on mock up.
Nice to have
• "RIVET STAPLES" as the main focus and Moravo Works full logo to be less prominent. Moravo Works emblem can also be a main focus, just not full logo. RIVET STAPLES on one line on front of box, maybe even just black box with black shiny lettering like TALLWIND do with their gift boxes.
Should not have
• Camouflage. Direct therapeutic claims ie. "Soothes sore muscles" instead use phrases like revitalize body if you are going to input any copy. Highly detailed imagery. Avoid using martial arts imagery or tacky symbols of helmets and stuff like that. This is a sleek modern minimalist design.

```html
<!DOCTYPE html>
<html lang="en">
<head>
<meta charset="utf-8">
<title>Rivet Staples Soap – Sleeve Die-line</title>
<link href="https://fonts.googleapis.com/css2?family=Jost:wght@400;500&family=Inter:wght@400;500&display=swap" rel="stylesheet">
<style>
  :root {
    --page: #ffffff;
    --sleeve: #d9d9d9;
    --ink: #8f8f8f;
    --ink-soft: #a0a0a0;
    --dieline: #8fd3e0;
  }
  * { box-sizing: border-box; margin: 0; padding: 0; }
  html, body { width: 1200px; height: 848px; overflow: hidden; background: var(--page); }
  .artboard { position: relative; width: 1200px; height: 848px; }
  .sleeve {
    position: absolute; left: 384px; top: 60px; width: 433px; height: 760px;
    background: var(--sleeve);
  }
  .dieline { position: absolute; left: 0; top: 0; width: 1200px; height: 848px; pointer-events: none; }
  .panel {
    position: absolute; left: 396px; width: 409px; padding: 0 20px;
    text-align: center; color: var(--ink);
  }
  .wordmark {
    top: 176px; font-family: 'Jost', sans-serif; font-weight: 500;
    font-size: 44px; letter-spacing: 0.04em; line-height: 1;
  }
  .net-weight {
    top: 292px; font-family: 'Inter', sans-serif; font-size: 8px;
    letter-spacing: 0.12em; color: var(--ink-soft);
  }
  .product-title {
    font-family: 'Jost', sans-serif; font-weight: 500; font-size: 15px;
    letter-spacing: 0.02em; line-height: 1;
  }
  .product-copy {
    font-family: 'Inter', sans-serif; font-size: 8.2px; line-height: 1.55;
    color: var(--ink-soft); margin-top: 11px;
  }
  .info-front { top: 350px; }
  .info-back { top: 708px; transform: rotate(180deg); }
  .back-details {
    top: 454px; font-family: 'Inter', sans-serif; font-size: 7.2px; line-height: 1.5;
    color: var(--ink-soft);
  }
  .detail-label {
    display: block; font-weight: 500; color: var(--ink); letter-spacing: 0.08em;
    font-size: 7.2px; margin-bottom: 1px;
  }
  .detail-block + .detail-block { margin-top: 7px; }
  .maker {
    top: 584px; display: flex; justify-content: center; align-items: center; gap: 6px;
    font-family: 'Inter', sans-serif; font-weight: 500; font-size: 13px; color: var(--ink-soft);
  }
  .maker-dot { width: 8px; height: 8px; border-radius: 50%; background: var(--ink-soft); }
  .back-footer {
    top: 618px; font-family: 'Inter', sans-serif; font-size: 7.2px; line-height: 1.6;
    color: var(--ink-soft);
  }
</style>
</head>
<body>
  <main class="artboard">
    <div class="sleeve"></div>

    <svg class="dieline" viewBox="0 0 1200 848" aria-hidden="true">
      <polygon points="402,39 799,39 805,74 396,74" fill="none" stroke="var(--dieline)" stroke-width="0.8"/>
      <rect x="396" y="74" width="409" height="733" fill="none" stroke="var(--dieline)" stroke-width="0.8"/>
      <g stroke="var(--dieline)" stroke-width="0.8" stroke-dasharray="3 3">
        <line x1="396" y1="74" x2="805" y2="74"/>
        <line x1="396" y1="319" x2="805" y2="319"/>
        <line x1="396" y1="441" x2="805" y2="441"/>
        <line x1="396" y1="686" x2="805" y2="686"/>
      </g>
    </svg>

    <div class="panel wordmark">RIVET STAPLES</div>
    <div class="panel net-weight">NET WT 100 g · 3.5 oz</div>

    <div class="panel info-front">
      <p class="product-title">RIVET STAPLES SOAP.</p>
      <p class="product-copy">Infused with magnesium, eucalyptus + tea tree oil, and activated charcoal.<br>A hydrating bar made to refresh skin and revitalise body after training.</p>
    </div>

    <div class="panel back-details">
      <div class="detail-block">
        <span class="detail-label">INGREDIENTS</span>
        Olive oil, coconut oil, shea butter, magnesium, activated charcoal,<br>eucalyptus oil, tea tree oil, peppermint oil, water, sodium hydroxide.
      </div>
      <div class="detail-block">
        <span class="detail-label">DIRECTIONS</span>
        Lather between wet hands and work over body after every session. Rinse well.
      </div>
      <div class="detail-block">
        <span class="detail-label">CAUTION</span>
        For external use only. Avoid contact with eyes. Stop use if irritation occurs.
      </div>
    </div>

    <div class="panel maker"><span class="maker-dot"></span>Moravo Works</div>

    <div class="panel back-footer">
      14 Larch Lane, Geelong VIC 3220 · rivetstaples.example<br>
      Made in Australia · NET WT 100 g
    </div>

    <div class="panel info-back">
      <p class="product-title">RIVET STAPLES SOAP.</p>
      <p class="product-copy">Infused with magnesium, eucalyptus + tea tree oil, and activated charcoal.<br>A hydrating bar made to refresh skin and revitalise body after training.</p>
    </div>
  </main>
</body>
</html>
```